Harborline Stay Collective Business Card Design

Design a business card for Harborline Stay Collective. Look at the website for colors and reference. Card should have logo, name, title, office number, mobile number, email, URL and a tagline like, "Luxury Hotel & Resort Email Marketing" (This might change).

https://www.harborlinestaycollective.net

The rest I will leave up to your imagination.

Contact Information for Business Card

Logo, name, title, office number, mobile number, email, URL and a tagline like, "Luxury Hotel & Resort Email Marketing" (This might change).

```html
<!DOCTYPE html>
<html lang="en">
<head>
<meta charset="utf-8">
<title>Harborline Stay Collective — Business Card</title>
<link rel="stylesheet" href="https://fonts.googleapis.com/css2?family=Open+Sans:wght@400;600;700&display=swap">
<style>
  :root {
    --stage: #8a8a88;
    --paper: #ffffff;
    --ink: #1b1b1b;
    --ink-soft: #555555;
    --accent: #f26a1b;
    --card-black: #1a1a1a;
  }
  * { box-sizing: border-box; margin: 0; padding: 0; }
  html, body { width: 1200px; height: 801px; overflow: hidden; }
  body {
    background: var(--stage);
    font-family: "Open Sans", Arial, sans-serif;
    display: flex;
    align-items: center;
    justify-content: center;
    gap: 40px;
  }
  .card {
    width: 540px;
    height: 309px;
    position: relative;
    border-bottom: 3px solid var(--accent);
    border-right: 3px solid var(--accent);
  }
  .card--front { background: var(--paper); }
  .card--back {
    background: var(--card-black);
    display: flex;
    align-items: center;
    justify-content: center;
    padding: 0 60px;
  }
  .brand {
    display: flex;
    align-items: center;
    gap: 10px;
    font-weight: 700;
    color: var(--ink);
    text-transform: uppercase;
    letter-spacing: 1px;
    line-height: 1.1;
  }
  .brand__square { width: 12px; height: 12px; background: var(--accent); flex: none; }
  .card--front .brand {
    position: absolute;
    left: 34px;
    top: 118px;
    width: 190px;
    font-size: 19px;
  }
  .card--back .brand {
    color: #ffffff;
    font-size: 23px;
    letter-spacing: 1.5px;
    gap: 12px;
    white-space: nowrap;
  }
  .card--back .brand__square { width: 14px; height: 14px; }
  .divider {
    position: absolute;
    left: 246px;
    top: 78px;
    width: 2px;
    height: 130px;
    background: var(--accent);
  }
  .contact {
    position: absolute;
    left: 266px;
    top: 80px;
  }
  .contact__name {
    color: var(--accent);
    font-weight: 700;
    font-size: 17px;
    letter-spacing: 0.5px;
    text-transform: uppercase;
  }
  .contact__title { color: var(--ink-soft); font-size: 13px; margin-bottom: 12px; }
  .contact__line {
    display: flex;
    align-items: center;
    gap: 7px;
    color: var(--ink-soft);
    font-size: 11.5px;
    line-height: 1.6;
  }
  .contact__line svg { width: 10px; height: 10px; flex: none; fill: var(--accent); }
  .tagline {
    position: absolute;
    right: 30px;
    bottom: 26px;
    color: var(--ink);
    font-size: 12.5px;
  }
</style>
</head>
<body>
  <section class="card card--front" aria-label="Card front">
    <div class="brand"><span class="brand__square"></span><span>Harborline Stay Collective</span></div>
    <div class="divider"></div>
    <div class="contact">
      <p class="contact__name">Daren Whitcombe</p>
      <p class="contact__title">President / CEO</p>
      <p class="contact__line">
        <svg viewBox="0 0 10 10" aria-hidden="true"><path d="M2 0.5 L3.8 2.6 L2.8 3.7 Q4 6 6.3 7.2 L7.4 6.2 L9.5 8 L8.2 9.5 Q2.5 8.5 0.5 1.8 Z"/></svg>
        555.014.2290
      </p>
      <p class="contact__line">
        <svg viewBox="0 0 10 10" aria-hidden="true"><path d="M0.5 2 H9.5 V8.5 H0.5 Z M0.5 2 L5 5.5 L9.5 2" stroke="#fff" stroke-width="0.8"/></svg>
        info@harborlinestaycollective.net
      </p>
      <p class="contact__line">
        <svg viewBox="0 0 10 10" aria-hidden="true"><circle cx="5" cy="5" r="4.5"/></svg>
        www.harborlinestaycollective.net
      </p>
    </div>
    <p class="tagline">Luxury Hotel &amp; Resort Email Marketing</p>
  </section>

  <section class="card card--back" aria-label="Card back">
    <div class="brand"><span class="brand__square"></span><span>Harborline Stay Collective</span></div>
  </section>
</body>
</html>
```